Custom Wordpress Theme - Original and Professional

We are a boutique IT consulting firm that provide small and medium business in Australia three different levels of IT service.
We are looking for a developer who will create a customised, original and professional wordpress theme. We are looking for the developer to create a professional, clean, clear and simple theme with a stylish layout, images and icons.
Our three services are: IT support | IT Services | IT Solutions and we would like to clearly differentiate the difference in each level of service in as few words as possible.
IT Support is the ad hock “call us, when you need us” service, that smaller business or those with minimal issues use.
IT service is the unlimited service, that business with existing (and well maintained) IT systems choose and is both flexible and scalable including no contracts or paperwork required.
IT solutions are the unlimited service that businesses that need new or updated infrastructure choose and it includes all the hardware, software and services with no contracts or any ongoing commitment.
The main page on the web site will attract the visitor to choose the right “service level” for their business and then we will have a dedicated page for each service and another page for a comparison (table) to compare all three services.
Lastly we will need a contact us page that has both office locations (Sydney and Melbourne), contact phone numbers and an email form.
Items we are focused on for this project are: 1. Images, 2.Icons 3. Layout.
In summary we are looking for a custom WordPress theme into a 6 page (Home, IT Support, IT Services, IT Solutions, Compare Service levels and Contact us) website. The design must include relevant images and icons and be clear, simple, professional and sleek.

Thank you for your time and creativity and I look forward to working with you!

Target Market(s)

Small and Medium businesses in Australia

Industry/Entity Type

Boutique

Requirements
Must have
• - 6 Pages layout: Home, IT support, IT services, IT Solutions, Compare service levels and Contact us
- Images, Layout and Icons.
- Clean, Clear, Simple, Elegant, Stylish.
Nice to have
• - Some text (if possible but not required).
Should not have
• - Complexity.
- Confusing layout.
- Generic non matching images and icons.

```html
<!DOCTYPE html>
<html lang="en">
<head>
<meta charset="utf-8">
<title>IT Support</title>
<link rel="stylesheet" href="https://fonts.googleapis.com/css2?family=Marcellus&family=Noto+Sans:wght@400&family=Ubuntu:wght@400&display=swap">
<style>
  :root {
    --ink: #111111;
    --muted: #8a8a8a;
    --accent: #3ad7e0;
    --accent-text: #2ec9d6;
    --bullet: #e04848;
    --rule: #c9ccd6;
    --footer: #3de0e6;
    --white: #ffffff;
    --hero-light: #f4f5f7;
    --hero-mid: #dcdfe4;
    --hero-blue: #b9cde6;
  }
  * { margin: 0; padding: 0; box-sizing: border-box; }
  html, body { width: 840px; height: 1200px; overflow: hidden; background: var(--white); }
  body { position: relative; font-family: "Noto Sans", sans-serif; color: var(--ink); }

  .brand { position: absolute; left: 45px; top: 54px; }
  .brand-name { font-family: "Marcellus", serif; font-size: 22px; letter-spacing: 0.3px; line-height: 1; }
  .brand-slogan { font-family: "Ubuntu", sans-serif; font-size: 8px; color: var(--muted); margin: 8px 0 0 19px; }

  .main-nav { position: absolute; top: 63px; left: 0; width: 840px; font-size: 12px; }
  .main-nav a { position: absolute; color: var(--ink); text-decoration: none; white-space: nowrap; }
  .main-nav a.is-current { color: var(--accent); font-family: "Ubuntu", sans-serif; font-weight: 300; }

  .header-rule { position: absolute; left: 35px; top: 118px; width: 770px; height: 1px;
    background: linear-gradient(90deg, var(--rule), #6d7590 20%, var(--rule) 60%, transparent); }

  .hero { position: absolute; left: 34px; top: 119px; width: 772px; height: 272px;
    background: linear-gradient(180deg, var(--white) 0%, var(--hero-light) 35%, var(--hero-mid) 100%); }
  .hero-visual { position: absolute; inset: 0; }
  .hero-caption { position: absolute; left: 16px; top: 189px; }
  .hero-title { font-family: "Marcellus", serif; font-size: 12px; color: #333; letter-spacing: 0.2px; }
  .breadcrumb { font-family: "Ubuntu", sans-serif; font-style: italic; font-size: 7px; margin: 6px 0 0 2px; color: #333; }
  .breadcrumb span { color: var(--accent); }

  .content { position: absolute; left: 45px; top: 521px; width: 533px; font-size: 11.8px; line-height: 20.2px; text-align: justify; }
  .content p + p { margin-top: 20.2px; }

  .sidebar { position: absolute; left: 607px; width: 200px; list-style: none; font-family: "Ubuntu", sans-serif; font-size: 7.8px; color: var(--accent-text); }
  .sidebar li { position: relative; padding-left: 11px; height: 22px; line-height: 12px; }
  .sidebar li::before { content: ""; position: absolute; left: 0; top: 3px; width: 6px; height: 7px;
    background: var(--bullet); clip-path: polygon(0 0, 45% 0, 100% 50%, 45% 100%, 0 100%, 55% 50%); }
  .sidebar.first { top: 517px; }
  .sidebar.second { top: 686px; }

  .site-footer { position: absolute; left: 0; top: 1153px; width: 840px; height: 47px; background: var(--footer); color: var(--white); }
  .footer-note { position: absolute; left: 54px; top: 15px; font-size: 12px; }
  .social-links { position: absolute; right: 39px; top: 20px; display: flex; gap: 4px; }
  .social-links span { width: 7px; height: 7px; border-radius: 50%; background: var(--white); }
</style>
</head>
<body>
  <header>
    <div class="brand">
      <div class="brand-name">COMPANY NAME</div>
      <div class="brand-slogan">YOUR COMPANY SOLGAN</div>
    </div>
    <nav class="main-nav">
      <a style="left:352px">Home</a>
      <a class="is-current" style="left:403px">IT support</a>
      <a style="left:475px">IT Services</a>
      <a style="left:548px">IT Solutions</a>
      <a style="left:628px">Compare Service</a>
      <a style="left:733px">Contact us</a>
    </nav>
    <div class="header-rule"></div>
  </header>

  <section class="hero">
    <svg class="hero-visual" role="img" aria-label="Banner photo: a worried man in a blue shirt beside a desk of network hardware and cables, with the headline Need help?" width="772" height="272" viewBox="0 0 772 272">
      <defs>
        <linearGradient id="heroFigure" x1="0" y1="0" x2="0" y2="1">
          <stop offset="0" stop-color="#e8edf3"/>
          <stop offset="1" stop-color="#b9cde6"/>
        </linearGradient>
        <linearGradient id="heroDesk" x1="0" y1="0" x2="0" y2="1">
          <stop offset="0" stop-color="#f7f7f8"/>
          <stop offset="1" stop-color="#d8dbe0"/>
        </linearGradient>
      </defs>
      <rect x="0" y="150" width="772" height="122" fill="url(#heroDesk)"/>
      <rect x="550" y="0" width="230" height="272" fill="url(#heroFigure)" opacity="0.7"/>
    </svg>
    <div class="hero-caption">
      <div class="hero-title">IT SUPPORT</div>
      <div class="breadcrumb">HOME | <span>IT SUPPORT</span></div>
    </div>
  </section>

  <main class="content">
    <p>Lorem ipsum dolor sit amet, consectetur adipiscing elit. Praesent nec euismod diam, ac gravida elit. In ac sagittis velit. Integer aliquet arcu ut dapibus bibendum. Donec non sodales purus. Maecenas in ipsum id ligula tempus egestas non at diam. Pellentesque sed lectus nisi. Sed commodo nunc lorem, quis pharetra tortor feugiat quis. Nullam in nisi suscipit nisi luctus semper. Proin hendrerit mauris non tempor facilisis. Pellentesque nec metus interdum, gravida erat sed, malesuada felis. Cras tincidunt nisi et auctor pellentesque. Donec sed augue in elit gravida mollis. Nam imperdiet lectus nec sapien consequat fringilla non sed lacus. Nam porta accumsan eros, id scelerisque nunc varius eget.</p>
    <p>Aliquam erat volutpat. Donec a leo dictum, dictum elit et, ornare lacus. Mauris tempor lacus est, quis cursus ipsum venenatis eget. Proin sollicitudin tristique sem ac faucibus. Pellentesque ut dignissim dui. Pellentesque gravida at velit id aliquet. Sed adipiscing varius mollis. In convallis hendrerit leo id gravida. Suspendisse facilisis blandit nisl eget blandit. Sed sit amet dignissim risus, ac luctus eros. Curabitur egestas vestibulum lacus. Etiam id vulputate turpis. Phasellus diam magna, pulvinar eget felis convallis, tincidunt rutrum purus. Morbi erat risus, cursus eleifend leo et, sagittis vestibulum risus. Ut vel dolor ac enim porttitor aliquet.</p>
  </main>

  <ul class="sidebar first">
    <li>Aenean nonummy hendrerit ma</li>
    <li>Fusce suscipit varius mi</li>
    <li>Cum sociis natoque penatibus</li>
    <li>Fusce feugiat malesuada odio</li>
    <li>Morbi nunc odio, gravida</li>
    <li>Morbi nunc odio, gravida</li>
  </ul>
  <ul class="sidebar second">
    <li>Aenean nonummy hendrerit ma</li>
    <li>Fusce suscipit varius mi</li>
    <li>Cum sociis natoque penatibus</li>
    <li>Fusce feugiat malesuada odio</li>
    <li>Morbi nunc odio, gravida</li>
    <li>Morbi nunc odio, gravida</li>
  </ul>

  <footer class="site-footer">
    <div class="footer-note">IT SOLUTION© 2013 • Privacy Policy</div>
    <div class="social-links" aria-label="Social links"><span></span><span></span><span></span><span></span></div>
  </footer>
</body>
</html>
```